Need Business Card for eLearning Company

Need a business card designed for our company, CareerTrellon.

CareerTrellon has developed a complete 12 lesson eLearning course to teach you the skills you need to present yourself in a job interview. The course uses advanced learning techniques in the multimedia videos, plus contains quizzes and additional exercises to insure you get the course and can walk into any interview with confidence and ease, and get the job.

www.careertrellon.com

Attached is our logo

Industry/Entity Type

Business

```html
<!DOCTYPE html>
<html lang="en">
<head>
<meta charset="utf-8">
<title>CareerTrellon Business Card</title>
<link href="https://fonts.googleapis.com/css2?family=Source+Sans+3:wght@300;400;600;700&display=swap" rel="stylesheet">
<style>
  :root {
    --backdrop: #1e1c1f;
    --card-white: #ffffff;
    --brand-purple: #8e1a7c;
    --brand-purple-light: #a4268f;
    --brand-green: #95b82a;
    --suit-grey: #4d4a4b;
    --ink: #3d3b3c;
    --ink-soft: #6a6769;
  }
  * { box-sizing: border-box; margin: 0; padding: 0; }
  html, body {
    width: 1200px;
    height: 675px;
    overflow: hidden;
    background: var(--backdrop);
    font-family: "Source Sans 3", "Helvetica Neue", Arial, sans-serif;
  }
  .stage {
    width: 1200px;
    height: 675px;
    display: flex;
    align-items: center;
    justify-content: center;
    gap: 60px;
  }
  .card {
    width: 525px;
    height: 300px;
    position: relative;
    overflow: hidden;
    box-shadow: 0 10px 30px rgba(0,0,0,0.45);
  }
  .card--front { background: var(--card-white); }
  .card--back {
    background: var(--brand-purple);
    display: flex;
    align-items: center;
    justify-content: center;
  }

  .illustration {
    position: absolute;
    top: 0;
    right: 0;
    width: 200px;
    height: 300px;
    background:
      linear-gradient(180deg,
        var(--brand-purple-light) 0%,
        var(--brand-green) 38%,
        var(--brand-purple-light) 60%,
        var(--suit-grey) 66%,
        var(--suit-grey) 100%);
    border-bottom-left-radius: 18px;
  }

  .wordmark {
    font-family: "Source Sans 3", "Helvetica Neue", Arial, sans-serif;
    font-weight: 400;
    color: var(--ink);
    letter-spacing: 0.5px;
  }
  .card--front .wordmark {
    position: absolute;
    left: 34px;
    top: 74px;
    font-size: 40px;
    line-height: 1;
  }
  .card--back .brand-lockup {
    display: flex;
    align-items: center;
    gap: 16px;
  }
  .card--back .brand-dot {
    width: 38px;
    height: 38px;
    border-radius: 50%;
    background: var(--ink);
  }
  .card--back .wordmark {
    font-size: 52px;
    line-height: 1;
    color: #231f22;
  }

  .contact {
    position: absolute;
    left: 40px;
    top: 138px;
    color: var(--ink-soft);
    font-weight: 300;
    font-size: 13px;
    line-height: 1.3;
  }
  .contact__name {
    color: var(--brand-purple);
    font-weight: 700;
    font-size: 17px;
    line-height: 1.1;
  }
  .contact__title {
    color: var(--ink);
    font-size: 14px;
    font-weight: 400;
    margin-bottom: 14px;
  }
  .contact__row {
    display: flex;
    align-items: center;
    gap: 6px;
  }
  .contact__row svg { width: 11px; height: 11px; fill: var(--brand-purple); flex: none; }
  .contact__web {
    margin-top: 6px;
    color: var(--brand-purple);
    font-weight: 700;
    font-size: 13px;
  }
</style>
</head>
<body>
<main class="stage">
  <section class="card card--front" aria-label="Business card front">
    <div class="illustration" role="img" aria-label="Illustration of purple and green speech bubbles rising above a figure in a grey suit and white tie"></div>
    <div class="wordmark">CareerTrellon</div>
    <div class="contact">
      <div class="contact__name">Marcus Delaine</div>
      <div class="contact__title">Principal</div>
      <div>418 N. Larkfield Avenue</div>
      <div>Denver, CO 80204</div>
      <div class="contact__row">
        <svg viewBox="0 0 12 12" aria-hidden="true"><path d="M2 1h2.5l1 3-1.5 1a6 6 0 0 0 3 3l1-1.5 3 1V11c-5 0-9-4-9-9z"/></svg>
        <span>555.214.8830</span>
      </div>
      <div class="contact__row">
        <svg viewBox="0 0 12 12" aria-hidden="true"><path d="M3 1h6v3H3z M1 5h10v5H1z M3 8h6v3H3z" /></svg>
        <span>555.307.6194</span>
      </div>
      <div class="contact__row">
        <svg viewBox="0 0 12 12" aria-hidden="true"><path d="M1 3h10v7H1z" /><path d="M1 3l5 4 5-4" fill="none" stroke="#fff" stroke-width="1"/></svg>
        <span>Marcus@careertrellon.com</span>
      </div>
      <div class="contact__web">www.careertrellon.com</div>
    </div>
  </section>

  <section class="card card--back" aria-label="Business card back">
    <div class="brand-lockup">
      <span class="brand-dot" aria-hidden="true"></span>
      <span class="wordmark">CareerTrellon</span>
    </div>
  </section>
</main>
</body>
</html>
```